Boutique town planning business needs a Business Card design

We need a business card design for a new company called The Zoning Bridgeway. We provide town planning and urban design services to government, business and community groups. We would like to see the designs use the colours in the logo (blue, deep red, green and amber), plenty of white and including black and grey in the writing. The final design should communicate collaboration, creativity and professionalism and that we are approachable.

```html
<!DOCTYPE html>
<html lang="en">
<head>
<meta charset="utf-8">
<title>The Zoning Bridgeway – Business Card</title>
<link rel="stylesheet" href="https://fonts.googleapis.com/css2?family=Roboto+Condensed:wght@400;700&display=swap">
<style>
  :root {
    --blue: #1e8fd6;
    --red: #b12a2e;
    --green: #2f9a45;
    --amber: #ee7d1c;
    --ink: #2b2b2b;
    --grey: #5f6266;
    --card: #ffffff;
    --backdrop: #e6e7e9;
    --mark-faint: #f1f1f2;
  }
  * { box-sizing: border-box; margin: 0; padding: 0; }
  html, body { width: 1200px; height: 675px; overflow: hidden; }
  body {
    background: var(--backdrop);
    font-family: "Roboto Condensed", "Arial Narrow", sans-serif;
    color: var(--ink);
    position: relative;
  }
  .card {
    position: absolute;
    top: 195px;
    width: 500px;
    height: 286px;
    background: var(--card);
    box-shadow: 0 6px 18px rgba(0,0,0,0.12);
    overflow: hidden;
  }
  .card--front { left: 70px; }
  .card--back { left: 630px; }

  .brand {
    display: flex;
    align-items: center;
    gap: 12px;
  }
  .brand__dot {
    flex: none;
    border-radius: 50%;
    background: var(--blue);
  }
  .brand__name {
    font-weight: 700;
    color: var(--ink);
    line-height: 1;
    white-space: nowrap;
  }
  .card--front .brand {
    position: absolute;
    left: 50%; top: 50%;
    transform: translate(-50%, -50%);
  }
  .card--front .brand__dot { width: 46px; height: 46px; }
  .card--front .brand__name { font-size: 38px; }

  .backdrop-circle {
    position: absolute;
    left: -70px; top: 40px;
    width: 330px; height: 330px;
    border-radius: 50%;
    background: var(--mark-faint);
  }
  .card--back .brand {
    position: absolute;
    right: 26px; top: 34px;
  }
  .card--back .brand__dot { width: 30px; height: 30px; }
  .card--back .brand__name { font-size: 24px; }

  .contact {
    position: absolute;
    left: 262px; top: 108px;
    list-style: none;
    font-size: 13px;
    color: var(--ink);
  }
  .contact li {
    display: flex;
    align-items: center;
    gap: 8px;
    height: 22px;
  }
  .contact svg { width: 13px; height: 13px; flex: none; fill: var(--red); }
  .contact .accent { color: var(--red); }

  .person {
    position: absolute;
    right: 250px; bottom: 62px;
    text-align: right;
  }
  .person__name {
    font-size: 18px;
    font-weight: 700;
    color: var(--red);
  }
  .person__role {
    font-size: 11.5px;
    color: var(--ink);
    margin-top: 1px;
  }
  .person__creds {
    font-size: 11.5px;
    color: var(--ink);
    margin-top: 6px;
    white-space: nowrap;
  }
</style>
</head>
<body>

  <section class="card card--front" aria-label="Business card front">
    <div class="brand">
      <span class="brand__dot"></span>
      <span class="brand__name">The Zoning Bridgeway</span>
    </div>
  </section>

  <section class="card card--back" aria-label="Business card back">
    <div class="backdrop-circle" aria-hidden="true"></div>

    <div class="brand">
      <span class="brand__dot"></span>
      <span class="brand__name">The Zoning Bridgeway</span>
    </div>

    <ul class="contact">
      <li>
        <svg viewBox="0 0 16 16" aria-hidden="true"><path d="M3 1h3l1.5 4-2 1.3a9 9 0 0 0 4.2 4.2L11 8.5l4 1.5v3a2 2 0 0 1-2 2C6.9 15 1 9.1 1 3a2 2 0 0 1 2-2z"/></svg>
        <span>0412 556 318</span>
      </li>
      <li>
        <svg viewBox="0 0 16 16" aria-hidden="true"><path d="M1 3h14v10H1zM2.5 4.5 8 9l5.5-4.5v-.2h-11z" fill-rule="evenodd"/></svg>
        <span>hello@zoningbridgeway.net</span>
      </li>
      <li>
        <svg viewBox="0 0 16 16" aria-hidden="true"><path d="M8 1a7 7 0 1 0 0 14A7 7 0 0 0 8 1zm0 1.5c.8 0 1.8 1.6 2.1 4H5.9C6.2 4.1 7.2 2.5 8 2.5zM5.9 9.5h4.2c-.3 2.4-1.3 4-2.1 4s-1.8-1.6-2.1-4zm-1.5-3H2.7a5.5 5.5 0 0 1 3.2-3.6c-.7 1-1.2 2.2-1.5 3.6zm0 3c.3 1.4.8 2.6 1.5 3.6a5.5 5.5 0 0 1-3.2-3.6zm7.2 0h1.7a5.5 5.5 0 0 1-3.2 3.6c.7-1 1.2-2.2 1.5-3.6zm0-3c-.3-1.4-.8-2.6-1.5-3.6a5.5 5.5 0 0 1 3.2 3.6z"/></svg>
        <span>www.<span class="accent">zoningbridgeway</span>.com.au</span>
      </li>
      <li>
        <svg viewBox="0 0 16 16" aria-hidden="true"><path d="M5 1h2l-.6 4h3l.6-4h2l-.6 4H14v2h-2.9l-.4 2H13v2h-2.6L9.8 15h-2l.6-4h-3L4.8 15h-2l.6-4H1V9h2.7l.4-2H2V5h2.4zm1.1 6-.4 2h3l.4-2z"/></svg>
        <span>ABN 51824736190</span>
      </li>
    </ul>

    <div class="person">
      <p class="person__name">Marisa Holloway</p>
      <p class="person__role">Director</p>
      <p class="person__creds">BPD (Urban Planning), GDipPD, MPIA, VPELA</p>
    </div>
  </section>

</body>
</html>
```